Design für 3-Monatskalender
Zielgruppe
Hallo, wir benötigen ein Design bzw. fertige Druckdaten für einen 3 Monatskalender mit den Feiertagen aus DE, AT und CH.
Format ist DIN A6, der Kalender wird benötigt für das Jahr 2024 und 2025.
Aufgabenstellung
Format: DIN A6
Kalendarium 2024 und 2025
Feiertage aus DE, AT und CH
Beispiel anbei, wichtig ist, das wir einen Magnetischen Ring als Datumsschieber nehmen. Der Ring hat die Maße: Durchmesser = 12mm Innendruchmesser = 10mm

```html
<!DOCTYPE html>
<html lang="de">
<head>
<meta charset="utf-8">
<title>3-Monatskalender Dezember 2024 – Februar 2025</title>
<link rel="stylesheet" href="https://fonts.googleapis.com/css2?family=League+Spartan:wght@800;900&family=Jost:wght@300&family=Oswald:wght@300;400;600&display=swap">
<style>
  :root {
    --sidebar: #879896;
    --sheet: #ecf0ee;
    --paper: #ffffff;
    --ink: #111111;
    --saturday: #8a9a98;
    --sunday: #d0114f;
    --title: #8a9a98;
    --rule: #111111;
  }
  * { margin: 0; padding: 0; box-sizing: border-box; }
  html, body { width: 851px; height: 1200px; overflow: hidden; background: var(--paper); }
  .calendar { position: relative; width: 851px; height: 1200px; background: var(--paper); }

  .sidebar { position: absolute; left: 0; top: 0; width: 180px; height: 1004px; background: var(--sidebar); }
  .sheet { position: absolute; left: 180px; width: 671px; background: var(--sheet); }
  .rule { position: absolute; left: 0; width: 851px; height: 1.3px; background: var(--rule); }

  .year {
    position: absolute; left: 18px; font-family: "Oswald", sans-serif; font-weight: 600;
    font-size: 47px; line-height: 1; color: var(--paper); letter-spacing: -1px;
  }
  .week-label, .day-head {
    position: absolute; font-family: "Oswald", sans-serif; font-weight: 300;
    font-size: 13.4px; line-height: 12.7px; letter-spacing: 0.1px;
  }
  .week-label { left: 131px; color: var(--paper); }
  .day-head { color: var(--ink); }
  .month-title {
    position: absolute; left: 214px; font-family: "League Spartan", sans-serif; font-weight: 800;
    font-size: 19px; color: var(--title); letter-spacing: 0.6px; line-height: 1;
  }

  .week {
    position: absolute; left: 0; width: 851px; height: 44px; line-height: 44px;
  }
  .week-no {
    position: absolute; right: 678px; font-family: "Jost", sans-serif; font-weight: 300;
    font-size: 30px; color: var(--paper);
  }
  .date {
    position: absolute; font-family: "League Spartan", sans-serif; font-weight: 900;
    font-size: 31px; color: var(--ink); top: 2px;
  }
  .date.sat { color: var(--saturday); }
  .date.sun { color: var(--sunday); }
  .c1 { left: 215px; } .c2 { left: 277px; } .c3 { left: 345px; } .c4 { left: 428px; }
  .c5 { left: 511px; } .c6 { left: 579px; } .c7 { left: 646px; }

  .date-ring { position: absolute; left: 405px; top: 177px; width: 88px; height: 88px; }

  .holidays { position: absolute; top: 1043px; font-family: "Oswald", sans-serif; font-weight: 300; }
  .holidays h2 { font-weight: 400; font-size: 12.5px; color: var(--sunday); margin-bottom: 3px; line-height: 16px; }
  .holidays dl { display: grid; font-size: 12px; line-height: 12.8px; color: var(--saturday); }
  .holidays dt, .holidays dd { white-space: nowrap; }
  .de { left: 131px; } .de dl { grid-template-columns: 58px auto; }
  .at { left: 369px; } .at dl { grid-template-columns: auto auto; column-gap: 4px; }
  .fr { left: 595px; } .fr dl { grid-template-columns: 58px auto; }
</style>
</head>
<body>
<main class="calendar">
  <div class="sidebar"></div>

  <div class="sheet" style="top:107px;height:266px"></div>
  <div class="sheet" style="top:463px;height:226px"></div>
  <div class="sheet" style="top:779px;height:225px"></div>
  <div class="rule" style="top:107px"></div>
  <div class="rule" style="top:463px"></div>
  <div class="rule" style="top:779px"></div>

  <!-- December 2024 -->
  <h1 class="month-title" style="top:35px">Dezember December Décembre</h1>
  <div class="year" style="top:58px">2024</div>
  <div class="week-label" style="top:62px">Woche<br>Week<br>Semaine</div>
  <div class="day-head c1" style="top:62px">Montag<br>Monday<br>Lundi</div>
  <div class="day-head c2" style="top:62px">Dienstag<br>Tuesday<br>Mardi</div>
  <div class="day-head c3" style="top:62px">Mittwoch<br>Wednesday<br>Mercredi</div>
  <div class="day-head c4" style="top:62px">Donnerstag<br>Thursday<br>Jeudi</div>
  <div class="day-head c5" style="top:62px">Freitag<br>Friday<br>Vendredi</div>
  <div class="day-head c6" style="top:62px">Samstag<br>Saturday<br>Samedi</div>
  <div class="day-head c7" style="top:62px">Sonntag<br>Sunday<br>Dimanche</div>

  <div class="week" style="top:113px"><span class="week-no">48</span><span class="date sun c7">1</span></div>
  <div class="week" style="top:157px"><span class="week-no">49</span><span class="date c1">2</span><span class="date c2">3</span><span class="date c3">4</span><span class="date c4">5</span><span class="date c5">6</span><span class="date sat c6">7</span><span class="date sun c7">8</span></div>
  <div class="week" style="top:200px"><span class="week-no">50</span><span class="date c1">9</span><span class="date c2">10</span><span class="date c3">11</span><span class="date c4">12</span><span class="date c5">13</span><span class="date sat c6">14</span><span class="date sun c7">15</span></div>
  <div class="week" style="top:244px"><span class="week-no">51</span><span class="date c1">16</span><span class="date c2">17</span><span class="date c3">18</span><span class="date c4">19</span><span class="date c5">20</span><span class="date sat c6">21</span><span class="date sun c7">22</span></div>
  <div class="week" style="top:288px"><span class="week-no">52</span><span class="date c1">23</span><span class="date c2">24</span><span class="date c3">25</span><span class="date c4">26</span><span class="date c5">27</span><span class="date sat c6">28</span><span class="date sun c7">29</span></div>
  <div class="week" style="top:331px"><span class="week-no">53</span><span class="date c1">30</span><span class="date c2">31</span></div>

  <svg class="date-ring" viewBox="0 0 88 88" aria-hidden="true">
    <circle cx="44" cy="44" r="40" fill="none" stroke="#d0114f" stroke-width="4"/>
  </svg>

  <!-- January 2025 -->
  <h1 class="month-title" style="top:391px">Januar January Janvier</h1>
  <div class="year" style="top:414px">2025</div>
  <div class="week-label" style="top:418px">Woche<br>Week<br>Semaine</div>
  <div class="day-head c1" style="top:418px">Montag<br>Monday<br>Lundi</div>
  <div class="day-head c2" style="top:418px">Dienstag<br>Tuesday<br>Mardi</div>
  <div class="day-head c3" style="top:418px">Mittwoch<br>Wednesday<br>Mercredi</div>
  <div class="day-head c4" style="top:418px">Donnerstag<br>Thursday<br>Jeudi</div>
  <div class="day-head c5" style="top:418px">Freitag<br>Friday<br>Vendredi</div>
  <div class="day-head c6" style="top:418px">Samstag<br>Saturday<br>Samedi</div>
  <div class="day-head c7" style="top:418px">Sonntag<br>Sunday<br>Dimanche</div>

  <div class="week" style="top:469px"><span class="week-no">1</span><span class="date c3">1</span><span class="date c4">2</span><span class="date c5">3</span><span class="date sat c6">4</span><span class="date sun c7">5</span></div>
  <div class="week" style="top:512px"><span class="week-no">2</span><span class="date c1">6</span><span class="date c2">7</span><span class="date c3">8</span><span class="date c4">9</span><span class="date c5">10</span><span class="date sat c6">11</span><span class="date sun c7">12</span></div>
  <div class="week" style="top:556px"><span class="week-no">3</span><span class="date c1">13</span><span class="date c2">14</span><span class="date c3">15</span><span class="date c4">16</span><span class="date c5">17</span><span class="date sat c6">18</span><span class="date sun c7">19</span></div>
  <div class="week" style="top:600px"><span class="week-no">4</span><span class="date c1">20</span><span class="date c2">21</span><span class="date c3">22</span><span class="date c4">23</span><span class="date c5">24</span><span class="date sat c6">25</span><span class="date sun c7">26</span></div>
  <div class="week" style="top:644px"><span class="week-no">5</span><span class="date c1">27</span><span class="date c2">28</span><span class="date c3">29</span><span class="date c4">30</span><span class="date c5">31</span></div>

  <!-- February 2025 -->
  <h1 class="month-title" style="top:707px">Februar February Février</h1>
  <div class="year" style="top:730px">2026</div>
  <div class="week-label" style="top:734px">Woche<br>Week<br>Semaine</div>
  <div class="day-head c1" style="top:734px">Montag<br>Monday<br>Lundi</div>
  <div class="day-head c2" style="top:734px">Dienstag<br>Tuesday<br>Mardi</div>
  <div class="day-head c3" style="top:734px">Mittwoch<br>Wednesday<br>Mercredi</div>
  <div class="day-head c4" style="top:734px">Donnerstag<br>Thursday<br>Jeudi</div>
  <div class="day-head c5" style="top:734px">Freitag<br>Friday<br>Vendredi</div>
  <div class="day-head c6" style="top:734px">Samstag<br>Saturday<br>Samedi</div>
  <div class="day-head c7" style="top:734px">Sonntag<br>Sunday<br>Dimanche</div>

  <div class="week" style="top:785px"><span class="week-no">5</span><span class="date sat c6">1</span><span class="date sun c7">2</span></div>
  <div class="week" style="top:828px"><span class="week-no">6</span><span class="date c1">3</span><span class="date c2">4</span><span class="date c3">5</span><span class="date c4">6</span><span class="date c5">7</span><span class="date sat c6">8</span><span class="date sun c7">9</span></div>
  <div class="week" style="top:872px"><span class="week-no">7</span><span class="date c1">10</span><span class="date c2">11</span><span class="date c3">12</span><span class="date c4">13</span><span class="date c5">14</span><span class="date sat c6">15</span><span class="date sun c7">16</span></div>
  <div class="week" style="top:916px"><span class="week-no">8</span><span class="date c1">17</span><span class="date c2">18</span><span class="date c3">19</span><span class="date c4">20</span><span class="date c5">21</span><span class="date sat c6">22</span><span class="date sun c7">23</span></div>
  <div class="week" style="top:960px"><span class="week-no">9</span><span class="date c1">24</span><span class="date c2">25</span><span class="date c3">26</span><span class="date c4">27</span><span class="date c5">28</span></div>

  <!-- Holidays -->
  <section class="holidays de">
    <h2>Feiertage in Deutschland</h2>
    <dl>
      <dt>Jan 01:</dt><dd>Neujahrstag</dd>
      <dt>Jan 06:</dt><dd>Offenbarung (BW, BY &amp; ST)</dd>
      <dt>Dez 25:</dt><dd>Weihnachtsfeiertag</dd>
      <dt>Dez 26:</dt><dd>Weihnachtsfeiertage</dd>
    </dl>
  </section>
  <section class="holidays at">
    <h2>Public Holidays of Austria</h2>
    <dl>
      <dt>01 January:</dt><dd>New Year's Day</dd>
      <dt>06 January:</dt><dd>Epiphany</dd>
      <dt>08 December:</dt><dd>Immaculate Conception</dd>
      <dt>24 December:</dt><dd>Christmas Eve</dd>
      <dt>25 December:</dt><dd>Christmas Day</dd>
      <dt>26 December:</dt><dd>Boxing Day</dd>
      <dt>31 December:</dt><dd>New Year</dd>
    </dl>
  </section>
  <section class="holidays fr">
    <h2>Jours fériés en France</h2>
    <dl>
      <dt>janv-01:</dt><dd>Jour de l'An</dd>
      <dt>déc-25:</dt><dd>Noël</dd>
      <dt>déc-26:</dt><dd>Saint-Étienne</dd>
    </dl>
  </section>
</main>
</body>
</html>
```